Seasons Greetings from Brackfold Hire.

Brackfold Hire is a Temporary Structures company based in South East London (South Bermondsey).
We dry hire Brackfold as well as deliver and manage projects with our own crew.
We are looking for someone to design our Christmas card or as I prefer to say ‘Season’s Greetings Card’ as this includes everyone religious or not.
The card should reflect Brackfold Hire Ltd and what we do, if you take a look at our website please look at the hires section only,
http://www.brackfold.co.uk/stage-hire.htm
Also take a look at our Brackfold Video’s
http://www.vidplume.example/user/firstbrackfold?feature=results_main
We would also like the card to be friendly and humorous,
Card Size: 210mm x 297mm folded to 210mm x 148mm
Suggested text for Front of card: Seasons Greetings from Brackfold Hire
Inner Text has yet to be confirmed but something like: Wishing you a Merry Christmas and a Happy New Year from everyone at Brackfold Hire
A clever use of the Brackfold logo or weave of the deck would be proffered. I have attached a PDF of a previous card.
Please DO Not show the Mantis Risers.
Please let me know if you require anymore info,
Target Market(s)
Brackfold Customers
Industry/Entity Type
Religious
Requirements
Must have
- Must be a professional looking card

```html
<!DOCTYPE html>
<html lang="en">
<head>
<meta charset="utf-8">
<title>Season's Greetings Card – Brackfold Hire</title>
<link rel="stylesheet" href="https://fonts.googleapis.com/css2?family=Pinyon+Script&family=Dancing+Script:wght@700&family=Roboto+Condensed:ital,wght@1,700&display=swap">
<style>
  :root {
    --page: #ffffff;
    --red-bright: #ee1c25;
    --red-mid: #c8141c;
    --red-deep: #8e0a10;
    --red-dark: #6e060b;
    --band-red: #d6171f;
    --white: #ffffff;
    --ink: #111111;
    --gold: #c9a030;
  }
  html, body {
    margin: 0;
    padding: 0;
    width: 1200px;
    height: 900px;
    overflow: hidden;
    background: var(--page);
  }
  .sheet { display: block; width: 1200px; height: 900px; }
  .script { font-family: "Pinyon Script", cursive; fill: var(--white); }
  .sign-off { font-family: "Dancing Script", cursive; font-weight: 700; }
  .panel-label {
    font-family: "Roboto Condensed", Arial, sans-serif;
    font-style: italic;
    font-weight: 700;
    font-size: 19px;
    fill: var(--ink);
  }
  .brand-name {
    font-family: "Pinyon Script", cursive;
    fill: var(--white);
  }
</style>
</head>
<body>
<svg class="sheet" viewBox="0 0 1200 900" xmlns="http://www.w3.org/2000/svg">
  <defs>
    <linearGradient id="outside-fill" x1="0" y1="0" x2="0" y2="1">
      <stop offset="0" stop-color="var(--red-bright)"/>
      <stop offset="0.5" stop-color="var(--red-deep)"/>
      <stop offset="1" stop-color="var(--red-bright)"/>
    </linearGradient>
    <radialGradient id="inside-fill" cx="0.5" cy="0.5" r="0.6">
      <stop offset="0" stop-color="var(--red-bright)"/>
      <stop offset="0.6" stop-color="var(--red-mid)"/>
      <stop offset="1" stop-color="var(--red-dark)"/>
    </radialGradient>
    <linearGradient id="photo-fill" x1="0" y1="0" x2="1" y2="1">
      <stop offset="0" stop-color="#f2b8a8"/>
      <stop offset="1" stop-color="#9c2a22"/>
    </linearGradient>
    <linearGradient id="bauble-fill" x1="0" y1="0" x2="1" y2="0">
      <stop offset="0" stop-color="var(--gold)"/>
      <stop offset="0.5" stop-color="#b3121a"/>
      <stop offset="1" stop-color="#d8252c"/>
    </linearGradient>
    <linearGradient id="bell-fill" x1="0" y1="0" x2="0" y2="1">
      <stop offset="0" stop-color="#e0262c"/>
      <stop offset="1" stop-color="var(--gold)"/>
    </linearGradient>
  </defs>

  <!-- Outside panel -->
  <g class="card card--outside">
    <polygon class="card-body" points="22,133 300,50 578,133 578,748 300,832 22,748" fill="url(#outside-fill)"/>
    <polygon class="deck-band deck-band--top" role="img" aria-label="Deck weave zigzag band"
             points="22,133 300,50 578,133 578,200 300,157 22,200" fill="var(--band-red)"/>
    <polygon class="deck-band deck-band--bottom" role="img" aria-label="Deck weave zigzag band"
             points="22,680 300,676 578,680 578,748 300,832 22,748" fill="var(--band-red)"/>
    <line class="fold-line" x1="22" y1="440" x2="578" y2="440" stroke="var(--red-dark)" stroke-opacity="0.4"/>

    <rect class="venue-photo" role="img" aria-label="Photo of a staged venue interior"
          x="234" y="258" width="130" height="88" fill="url(#photo-fill)" stroke="#f0c0b0" stroke-width="1"/>

    <text class="script greeting" font-size="74">
      <tspan x="92" y="542">Season's</tspan>
      <tspan x="205" y="602">Greetings</tspan>
    </text>
    <rect class="baubles" role="img" aria-label="Christmas baubles with red ribbon"
          x="372" y="498" width="142" height="60" rx="28" fill="url(#bauble-fill)"/>

    <g class="brand-mark">
      <rect x="256" y="670" width="12" height="12" fill="var(--white)"/>
      <text class="brand-name" x="274" y="684" font-size="20">Brackfold</text>
    </g>
    <text class="brand-name from-line" x="365" y="696" font-size="20" transform="rotate(-9 365 696)">From Brackfold Hire</text>

    <text class="panel-label" x="22" y="848">Greetings Card Outside</text>
  </g>

  <!-- Inside panel -->
  <g class="card card--inside">
    <polygon class="card-body" role="img" aria-label="Red damask patterned background"
             points="624,133 904,50 1180,133 1180,748 904,832 624,748" fill="url(#inside-fill)"/>
    <rect class="bells" role="img" aria-label="Golden bells tied with a red bow"
          x="818" y="158" width="136" height="130" rx="40" fill="url(#bell-fill)"/>

    <text class="script wishes" text-anchor="middle">
      <tspan x="904" y="362" font-size="92">Merry</tspan>
      <tspan x="904" y="444" font-size="92">Christmas</tspan>
      <tspan x="904" y="522" font-size="70">&amp;</tspan>
      <tspan x="904" y="584" font-size="64">a Happy New Year</tspan>
    </text>

    <rect class="sign-off-band" x="624" y="633" width="556" height="49" fill="var(--white)"/>
    <text class="sign-off" x="902" y="668" text-anchor="middle" font-size="30" fill="var(--red-bright)">from everyone at Brackfold Hire</text>

    <text class="panel-label" x="626" y="848">Greetings Card Inside</text>
  </g>
</svg>
</body>
</html>
```